Designs of screens for job search mobile app

Design the following screens:

1. Login
2. Job search results in tabs
3. Job details in cards format
4. Profile
5. Settings

Logo and references are provided. The app need to be playful, easy to use, different from traditional job search app like Workvane, ProLattice and others and targeted to Millennial users (age 18-30).

The main app reference is Piqto, in terms of the colorful and fun color and font scheme.

Target Market(s)

Millennial users (age 18-30).

Requirements
Must have
• A fun, playful feel

```html
<!DOCTYPE html>
<html lang="en">
<head>
<meta charset="utf-8">
<title>JobRover – App Screens</title>
<link href="https://fonts.googleapis.com/css2?family=Mulish:wght@400;600;700;800&display=swap" rel="stylesheet">
<style>
:root{
  --canvas:#e4e4e4;
  --teal:#02b8b0;
  --teal-soft:#b2ebe7;
  --teal-mid:#62d1ca;
  --paper:#f2f2f2;
  --card:#ffffff;
  --ink:#333333;
  --ink-soft:#555555;
  --line:#d9d9d9;
  --orange:#f26a1b;
  --navy:#2f4f8f;
}
*{box-sizing:border-box;margin:0;padding:0}
html,body{width:1200px;height:1200px;overflow:hidden;background:var(--canvas);font-family:"Mulish",sans-serif;color:var(--ink)}
.stage{position:absolute;left:0;top:0;width:1500px;height:1500px;transform:scale(.8);transform-origin:0 0}
.phone{position:absolute;width:312px;height:554px;background:var(--paper);overflow:hidden;box-shadow:0 1px 3px rgba(0,0,0,.12)}
.phone.teal{background:var(--teal)}
.abs{position:absolute}
.status{position:absolute;left:0;top:0;width:100%;height:16px;color:#fff;font-size:8px;display:flex;align-items:center;padding:0 6px}
.status .carrier{flex:1}
.status .clock{position:absolute;left:0;right:0;text-align:center}
.status .battery{display:flex;align-items:center;gap:4px}
.status .battery i{display:inline-block;width:16px;height:7px;background:#fff;border-radius:1px}
.appbar{position:absolute;left:0;top:0;width:100%;height:48px;background:var(--teal)}
.appbar .title{position:absolute;left:0;right:0;top:25px;text-align:center;color:#fff;font-size:12px;font-weight:600}
.appbar .back{position:absolute;left:6px;top:23px}
.label{position:absolute;color:var(--teal);font-size:14px;font-weight:600;letter-spacing:.2px}
.field{position:absolute;height:34px;background:var(--card);border:1px solid var(--line);border-radius:2px;font-size:13px;padding:0 8px;display:flex;align-items:center;color:var(--ink)}
.field .clear{position:absolute;right:7px;top:7px;width:20px;height:20px;border-radius:50%;background:#dcdcdc}
.divider{position:absolute;left:0;width:100%;height:1px;background:#d6d6d6}
.btn{position:absolute;background:var(--teal);color:#fff;font-size:13px;font-weight:600;display:flex;align-items:center;justify-content:center;border-radius:2px}
.job-card{position:absolute;left:7px;width:298px;background:var(--card);border-radius:3px;box-shadow:0 1px 2px rgba(0,0,0,.1)}
.job-card .ago{position:absolute;right:7px;top:4px;color:var(--orange);font-size:11px}
.job-card .company{position:absolute;left:6px;width:96px;text-align:center;font-size:11px;font-weight:700;color:var(--ink)}
.job-card .company b{display:block;font-size:17px;font-weight:800;color:var(--navy);margin-bottom:4px}
.job-card .info{position:absolute;left:106px;font-size:13px;line-height:17.5px;color:var(--ink-soft)}
.job-card .info h3{font-size:15px;font-weight:800;color:var(--teal);line-height:18px}
.tabbar{position:absolute;left:0;bottom:0;width:100%;height:46px;background:var(--card);display:flex;justify-content:space-around;align-items:center;border-top:1px solid #e4e4e4}
.settings-group{position:absolute;left:7px;width:298px;background:var(--card);box-shadow:0 1px 2px rgba(0,0,0,.08)}
.settings-group .row{height:30px;border-bottom:1px solid #e2e2e2;padding-left:10px;font-size:14px;display:flex;align-items:center;color:var(--ink)}
.settings-group .row:last-child{border-bottom:0}
.toggle{position:absolute;right:8px;width:42px;height:20px;border-radius:10px;font-size:8px;color:#fff;font-weight:700;display:flex;align-items:center}
.toggle.on{background:var(--teal);padding-left:4px}
.toggle.on::after{content:"";position:absolute;right:1px;top:1px;width:18px;height:18px;border-radius:50%;background:#fff}
.toggle.off{background:var(--orange);justify-content:flex-end;padding-right:4px}
.toggle.off::after{content:"";position:absolute;left:1px;top:1px;width:18px;height:18px;border-radius:50%;background:#fff}
.friend{position:absolute;width:44px;text-align:center}
.friend .avatar{width:44px;height:44px;border-radius:50%;background:linear-gradient(135deg,#a98b6f,#4a3a30)}
.friend span{display:block;margin-top:10px;font-size:13px;color:var(--ink)}
.round-action{position:absolute;width:44px;height:44px;border-radius:50%;background:#fff;display:flex;align-items:center;justify-content:center}
</style>
</head>
<body>
<div class="stage">

  <!-- Login -->
  <section class="phone teal" style="left:143px;top:127px">
    <div class="abs" style="left:0;right:0;top:52px;display:flex;justify-content:center;align-items:center;gap:8px;color:#fff;font-size:30px;font-weight:600">
      <span style="width:30px;height:30px;border-radius:50%;background:#fff;display:inline-block"></span>JobRover
    </div>
    <div class="abs" role="img" aria-label="Illustration of a camper van on a hill under clouds" style="left:27px;top:142px;width:258px;height:263px;background:linear-gradient(180deg,var(--teal-soft) 0%,var(--teal-soft) 78%,var(--teal-mid) 100%);box-shadow:0 1px 3px rgba(0,0,0,.15)"></div>
    <div class="abs" style="left:141px;top:446px;display:flex;gap:4px">
      <i style="width:6px;height:6px;border-radius:50%;background:#b9ece8"></i><i style="width:6px;height:6px;border-radius:50%;background:#fff"></i><i style="width:6px;height:6px;border-radius:50%;background:#b9ece8"></i>
    </div>
    <div class="btn" style="left:27px;top:491px;width:258px;height:37px;background:var(--navy);font-weight:400">Login with Friendloop</div>
  </section>

  <!-- Profile -->
  <section class="phone" style="left:603px;top:127px">
    <header class="appbar">
      <div class="status"><span class="carrier">●●●○○ Strokei</span><span class="clock">12:37 pm</span><span class="battery">80% <i></i></span></div>
      <svg class="back" width="10" height="16" viewBox="0 0 10 16"><path d="M8 1 2 8l6 7" fill="none" stroke="#fff" stroke-width="1.6"/></svg>
      <div class="title">Profile</div>
    </header>
    <div class="label" style="left:7px;top:56px">First Name</div>
    <div class="label" style="left:160px;top:56px">Last Name</div>
    <div class="field" style="left:7px;top:77px;width:144px">John</div>
    <div class="field" style="left:160px;top:77px;width:144px">Doe</div>
    <div class="label" style="left:7px;top:118px">Email</div>
    <div class="label" style="left:160px;top:118px">Gender</div>
    <div class="field" style="left:7px;top:140px;width:144px">john@postbox.com</div>
    <div class="field" style="left:160px;top:140px;width:144px">Male
      <svg class="abs" style="right:0;top:0" width="30" height="32" viewBox="0 0 30 32"><path d="M0 0v32" stroke="#d9d9d9"/><path d="M9 12h12l-6 9z" fill="#333"/></svg>
    </div>
    <div class="label" style="left:7px;top:182px">Birthday</div>
    <div class="label" style="left:160px;top:182px">City</div>
    <div class="field" style="left:7px;top:203px;width:144px">30 Oct 1973</div>
    <div class="field" style="left:160px;top:203px;width:144px">Singapore</div>
    <div class="label" style="left:7px;top:245px">State</div>
    <div class="label" style="left:160px;top:245px">Country</div>
    <div class="field" style="left:7px;top:266px;width:144px">Singapore</div>
    <div class="field" style="left:160px;top:266px;width:144px">Singapore</div>
    <div class="divider" style="top:319px"></div>
    <div class="label" style="left:7px;top:330px">Headline</div>
    <div class="field" style="left:7px;top:351px;width:298px">Write a headline about me</div>
    <div class="label" style="left:7px;top:390px">Summary</div>
    <div class="field" style="left:7px;top:411px;width:298px;height:90px"></div>
    <div class="btn" style="left:7px;top:509px;width:298px;height:38px">Search Jobs</div>
  </section>

  <!-- Skills -->
  <section class="phone" style="left:1043px;top:127px">
    <header class="appbar">
      <div class="status"><span class="carrier">●●●○○ Strokei</span><span class="clock">12:37 pm</span><span class="battery">80% <i></i></span></div>
      <svg class="back" width="10" height="16" viewBox="0 0 10 16"><path d="M8 1 2 8l6 7" fill="none" stroke="#fff" stroke-width="1.6"/></svg>
      <div class="title">Skills</div>
    </header>
    <div class="label" style="left:7px;top:56px">Marketing</div>
    <div class="field" style="left:7px;top:77px;width:207px">Marketing</div>
    <div class="btn" style="left:223px;top:77px;width:81px;height:34px;font-weight:400">Add</div>
    <div class="divider" style="top:137px"></div>
    <div class="label" style="left:7px;top:151px">Python</div>
    <div class="field" style="left:7px;top:173px;width:298px">Python
      <svg class="clear" viewBox="0 0 20 20"><path d="M6 6l8 8M14 6l-8 8" stroke="#222" stroke-width="1.6"/></svg></div>
    <div class="label" style="left:7px;top:213px">Business Development</div>
    <div class="field" style="left:7px;top:235px;width:298px">Business Development
      <svg class="clear" viewBox="0 0 20 20"><path d="M6 6l8 8M14 6l-8 8" stroke="#222" stroke-width="1.6"/></svg></div>
    <div class="label" style="left:7px;top:276px">C#</div>
    <div class="field" style="left:7px;top:297px;width:298px">C#
      <svg class="clear" viewBox="0 0 20 20"><path d="M6 6l8 8M14 6l-8 8" stroke="#222" stroke-width="1.6"/></svg></div>
    <div class="btn" style="left:7px;top:509px;width:298px;height:38px;font-weight:400">Save</div>
  </section>

  <!-- Search results -->
  <section class="phone" style="left:143px;top:837px">
    <header class="appbar">
      <div class="status"><span class="carrier">●●●○○ Strokei</span><span class="clock">12:37 pm</span><span class="battery">80% <i></i></span></div>
      <svg class="back" width="10" height="16" viewBox="0 0 10 16"><path d="M8 1 2 8l6 7" fill="none" stroke="#fff" stroke-width="1.6"/></svg>
      <div class="title">Search</div>
    </header>
    <div class="abs" style="left:12px;top:61px;font-size:17px;color:#444">Search Results</div>
    <article class="job-card" style="top:95px;height:95px">
      <span class="ago">18 hrs ago</span>
      <div class="company" style="top:24px"><b>Brightcore</b>BRIGHTCORE</div>
      <div class="info" style="top:19px"><h3>Software Engineers</h3>Singapore<br>$80k - $90k per annum</div>
    </article>
    <article class="job-card" style="top:198px;height:96px">
      <span class="ago">2 hrs ago</span>
      <div class="company" style="top:28px"><b>Ridgeway</b>RIDGEWAY MOTORS</div>
      <div class="info" style="top:18px"><h3>System Archiect</h3>Singapore<br>$100k - $120k per annum<br>3 friends work / worked here</div>
    </article>
    <article class="job-card" style="top:302px;height:96px">
      <span class="ago">1 day ago</span>
      <div class="company" style="top:28px"><b style="font-size:15px;color:#c0392b">Broth &amp; Co</b>BROTH &amp; CO</div>
      <div class="info" style="top:19px"><h3>System Archiect</h3>Singapore<br>$90k - $100k per annum</div>
    </article>
    <article class="job-card" style="top:405px;height:95px">
      <span class="ago">19 days ago</span>
      <div class="company" style="top:28px"><b>Solano</b>SOLANO SYSTEMS</div>
      <div class="info" style="top:19px"><h3>Java Developer</h3>Singapore<br>$115k per annum</div>
    </article>
    <nav class="tabbar">
      <svg width="22" height="22" viewBox="0 0 22 22"><path d="M11 2 1 11h3v9h5v-6h4v6h5v-9h3z" fill="#444"/></svg>
      <svg width="22" height="22" viewBox="0 0 22 22"><circle cx="9" cy="9" r="6" fill="none" stroke="var(--teal)" stroke-width="3"/><path d="M13 13l7 7" stroke="var(--teal)" stroke-width="3.5"/></svg>
      <svg width="22" height="22" viewBox="0 0 22 22"><circle cx="11" cy="7" r="5" fill="#444"/><path d="M2 21c0-6 4-8 9-8s9 2 9 8z" fill="#444"/></svg>
      <svg width="22" height="22" viewBox="0 0 22 22"><rect x="4" y="3" width="14" height="18" rx="1" fill="#444"/><rect x="8" y="1" width="6" height="4" fill="#444"/></svg>
      <svg width="22" height="22" viewBox="0 0 22 22"><circle cx="11" cy="11" r="7.5" fill="none" stroke="#444" stroke-width="4" stroke-dasharray="3 2.9"/><circle cx="11" cy="11" r="5" fill="none" stroke="#444" stroke-width="3"/></svg>
    </nav>
  </section>

  <!-- Job details -->
  <section class="phone teal" style="left:603px;top:837px">
    <div class="status"><span class="carrier">●●●○○ Strokei</span><span class="clock">12:37 pm</span><span class="battery">80% <i></i></span></div>
    <svg class="abs" style="left:7px;top:25px" width="12" height="12" viewBox="0 0 12 12"><path d="M1 1l10 10M11 1 1 11" stroke="#fff" stroke-width="1.8"/></svg>
    <div class="abs" style="left:0;right:0;top:25px;text-align:center;color:#fff;font-size:12px;font-weight:600">Job Details</div>
    <svg class="abs" style="left:288px;top:22px" width="16" height="18" viewBox="0 0 16 18"><path d="M5 6H2v11h12V6h-3M8 12V1M4 5l4-4 4 4" fill="none" stroke="#fff" stroke-width="1.4"/></svg>
    <div class="abs" style="left:65px;top:72px;width:182px;height:14px;background:#9fe2dd;border-radius:3px 3px 0 0"></div>
    <div class="abs" style="left:45px;top:80px;width:222px;height:14px;background:#cdf2ef;border-radius:3px 3px 0 0"></div>
    <article class="abs" style="left:25px;top:92px;width:262px;height:364px;background:#fff;border-radius:3px;box-shadow:0 1px 3px rgba(0,0,0,.15)">
      <span class="abs" style="right:6px;top:7px;color:var(--orange);font-size:11px">18 hrs ago</span>
      <div class="abs" style="left:6px;top:26px;width:78px;text-align:center;font-size:9px;font-weight:700"><b style="display:block;font-size:14px;font-weight:800;color:var(--navy);margin-bottom:3px">Ridgeway</b>RIDGEWAY MOTORS</div>
      <div class="abs" style="left:83px;top:23px;font-size:13px;line-height:17.5px;color:var(--ink-soft)"><h3 style="font-size:15px;font-weight:800;color:var(--teal);line-height:18px">Software Engineers</h3>Singapore<br>$80k - $90k per annum</div>
      <div class="divider" style="top:80px;background:#e0e0e0"></div>
      <div class="abs" style="left:0;right:0;top:86px;text-align:center;color:var(--teal);font-weight:800;font-size:15px">Friends working / worked here</div>
      <div class="friend" style="left:34px;top:111px"><div class="avatar" role="img" aria-label="Profile photo of Lucy"></div><span>Lucy</span></div>
      <div class="friend" style="left:108px;top:111px"><div class="avatar" role="img" aria-label="Profile photo of Boris"></div><span>Boris</span></div>
      <div class="friend" style="left:181px;top:111px"><div class="avatar" role="img" aria-label="Profile photo of Bryant"></div><span>Bryant</span></div>
      <div class="divider" style="top:184px;background:#e0e0e0"></div>
      <div class="abs" style="left:0;right:0;top:196px;text-align:center;color:var(--teal);font-weight:800;font-size:15px">Job description</div>
      <p class="abs" style="left:22px;right:22px;top:221px;text-align:center;font-size:13px;line-height:17px;color:var(--ink-soft)">It is a long established fact that a readerwill be distracted by the readable content of a page when looking at its layout. The point of using Lorem Ipsum...</p>
      <div class="abs" style="left:0;right:0;top:317px;text-align:center;font-size:14px;line-height:21px;color:var(--ink)">Skills:<br>Python, PHP, C#</div>
    </article>
    <div class="round-action" style="left:55px;top:484px"><svg width="20" height="20" viewBox="0 0 20 20"><path d="M4 2l7 8-7 8M10 2l7 8-7 8" fill="none" stroke="var(--teal)" stroke-width="1.6"/></svg></div>
    <div class="round-action" style="left:133px;top:484px"><svg width="20" height="20" viewBox="0 0 20 20"><rect x="2" y="2" width="16" height="16" rx="1" fill="none" stroke="var(--teal)" stroke-width="2"/><rect x="6" y="3" width="8" height="5" fill="var(--teal)"/><rect x="5" y="11" width="10" height="6" fill="none" stroke="var(--teal)" stroke-width="1.5"/></svg></div>
    <div class="round-action" style="left:211px;top:484px"><svg width="22" height="20" viewBox="0 0 22 20"><path d="M2 10l6 6L20 3" fill="none" stroke="var(--teal)" stroke-width="2.4"/></svg></div>
  </section>

  <!-- Settings -->
  <section class="phone" style="left:1043px;top:837px">
    <header class="appbar">
      <div class="status"><span class="carrier">●●●○○ Strokei</span><span class="clock">12:37 pm</span><span class="battery">80% <i></i></span></div>
      <div class="title">Settings</div>
    </header>
    <div class="settings-group" style="top:56px">
      <div class="row" style="height:34px;color:var(--teal);font-weight:800;font-size:15px">Notifications</div>
      <div class="row" style="height:43px;font-size:13px;position:relative">Job Messages<span class="toggle on" style="top:11px">ON</span></div>
      <div class="row" style="height:43px;font-size:13px;position:relative">Send Notifications by Email Too<span class="toggle off" style="top:11px">OFF</span></div>
    </div>
    <div class="settings-group" style="top:185px">
      <div class="row">Like Us On Friendloop</div>
      <div class="row">Share on ProLattice</div>
      <div class="row">Follow on Chirpline</div>
      <div class="row">Rate Us on App Market</div>
    </div>
    <div class="settings-group" style="top:313px">
      <div class="row">Help</div>
      <div class="row">Privacy Policy</div>
      <div class="row">Terms of Use</div>
    </div>
    <div class="btn" style="left:7px;top:428px;width:298px;height:37px;font-weight:400">Logout</div>
    <div class="abs" style="left:0;right:0;top:486px;text-align:center;font-size:13px;color:#444">Version 1.2</div>
    <nav class="tabbar">
      <svg width="22" height="22" viewBox="0 0 22 22"><path d="M11 2 1 11h3v9h5v-6h4v6h5v-9h3z" fill="#444"/></svg>
      <svg width="22" height="22" viewBox="0 0 22 22"><circle cx="9" cy="9" r="6" fill="none" stroke="#444" stroke-width="3"/><path d="M13 13l7 7" stroke="#444" stroke-width="3.5"/></svg>
      <svg width="22" height="22" viewBox="0 0 22 22"><circle cx="11" cy="7" r="5" fill="#444"/><path d="M2 21c0-6 4-8 9-8s9 2 9 8z" fill="#444"/></svg>
      <svg width="22" height="22" viewBox="0 0 22 22"><rect x="4" y="3" width="14" height="18" rx="1" fill="#444"/><rect x="8" y="1" width="6" height="4" fill="#444"/></svg>
      <svg width="22" height="22" viewBox="0 0 22 22"><circle cx="11" cy="11" r="7.5" fill="none" stroke="var(--teal)" stroke-width="4" stroke-dasharray="3 2.9"/><circle cx="11" cy="11" r="5" fill="none" stroke="var(--teal)" stroke-width="3"/></svg>
    </nav>
  </section>

</div>
</body>
</html>
```